Executive Coaching and Spiritual Development Company needs a business card design.

We need a business card design for our company. We already have a logo that was created through Inkharbor that we will submit and would like to see this work on black, blue and white backgrounds. Our personal information should be included as well. The design should communicate trust, spirituality, support and partnership.

Industry/Entity Type

Business

Colors
0255a3
33a6d7
ffffff
000000
474747

Requirements
Nice to have
• The colors offered here are just ideas--we are open to other suggestions, too.

```html
<!DOCTYPE html>
<html lang="en">
<head>
<meta charset="UTF-8">
<title>Innerway Business Card</title>
<link href="https://fonts.googleapis.com/css2?family=Didact+Gothic&display=swap" rel="stylesheet">
<style>
  :root {
    --backdrop: #2a2a2c;
    --navy: #0f2533;
    --navy-light: #1d3a4b;
    --paper: #ffffff;
    --ink: #132634;
    --text-grey: #5c6166;
    --stripe-blue: #9fb3dc;
    --stripe-orange: #f2a56a;
    --stripe-green: #8cc66a;
    --ring: #9aa0a6;
  }
  * { box-sizing: border-box; margin: 0; padding: 0; }
  html, body {
    width: 1200px; height: 900px; overflow: hidden;
    background: var(--backdrop);
    font-family: "Didact Gothic", "Century Gothic", sans-serif;
  }
  .stage {
    position: relative; width: 1200px; height: 900px;
  }
  .card {
    position: absolute; top: 307px;
    width: 500px; height: 286px;
    overflow: hidden;
    box-shadow: 0 12px 30px rgba(0,0,0,.45);
  }
  /* Front side */
  .card-front {
    left: 80px;
    background: linear-gradient(160deg, var(--navy-light) 0%, var(--navy) 60%);
  }
  .front-identity {
    position: absolute; right: 30px; bottom: 58px;
    display: flex; align-items: center; gap: 10px;
  }
  .brand-dot {
    width: 30px; height: 30px; border-radius: 50%;
    border: 2px solid var(--paper);
  }
  .front-brand {
    color: var(--paper); font-size: 28px; line-height: 1;
  }
  .front-url {
    position: absolute; right: 30px; bottom: 36px;
    color: var(--paper); font-size: 13px; letter-spacing: .5px;
  }
  /* Back side */
  .card-back {
    left: 620px; background: var(--paper);
  }
  .back-band {
    position: absolute; left: 0; top: 0; bottom: 0; width: 90px;
    background: linear-gradient(180deg, var(--navy-light), var(--navy));
  }
  .back-stripes {
    position: absolute; left: 90px; top: 0; bottom: 0; width: 18px;
    background: linear-gradient(90deg,
      var(--stripe-blue) 0 4px, var(--paper) 4px 7px,
      var(--stripe-orange) 7px 11px, var(--paper) 11px 14px,
      var(--stripe-green) 14px 18px);
  }
  .back-mark {
    position: absolute; left: 58px; top: 62px;
    width: 66px; height: 66px; border-radius: 50%;
    background: var(--paper); border: 2px solid var(--ring);
  }
  .back-brand {
    position: absolute; left: 138px; top: 66px;
    color: var(--ink); font-size: 40px; line-height: 1;
  }
  .contact {
    position: absolute; left: 150px; top: 122px;
    color: var(--text-grey); font-size: 14px; line-height: 18px;
    list-style: none;
  }
  .contact .name { color: var(--ink); }
  .contact li { display: flex; align-items: center; gap: 7px; }
  .contact svg { width: 11px; height: 11px; fill: var(--ink); flex: none; }
</style>
</head>
<body>
<main class="stage">
  <section class="card card-front" aria-label="Card front">
    <div class="front-identity">
      <span class="brand-dot"></span>
      <span class="front-brand">Innerway</span>
    </div>
    <p class="front-url">www.innerway.com</p>
  </section>

  <section class="card card-back" aria-label="Card back">
    <div class="back-band"></div>
    <div class="back-stripes"></div>
    <span class="back-mark"></span>
    <h1 class="back-brand">Innerway</h1>
    <ul class="contact">
      <li class="name">Your Name</li>
      <li>President</li>
      <li>18 Quiet Lane</li>
      <li>Fairbrook, CA 90000</li>
      <li>
        <svg viewBox="0 0 12 12" aria-hidden="true"><path d="M2 1h3l1 3-2 1a7 7 0 0 0 3 3l1-2 3 1v3c-6 0-9-3-9-9z"/></svg>
        555-010-4150
      </li>
      <li>
        <svg viewBox="0 0 12 12" aria-hidden="true"><rect x="2" y="1" width="8" height="4"/><rect x="1" y="5" width="10" height="4"/><rect x="3" y="9" width="6" height="2"/></svg>
        555-010-4150
      </li>
      <li>
        <svg viewBox="0 0 12 12" aria-hidden="true"><path d="M1 2h10v8H1z M1 2l5 4 5-4" fill="none" stroke="currentColor" stroke-width="1.4" style="stroke:var(--ink)"/></svg>
        info@innerway.com
      </li>
      <li>
        <svg viewBox="0 0 12 12" aria-hidden="true"><circle cx="6" cy="6" r="5" fill="none" stroke-width="1.2" style="stroke:var(--ink)"/><path d="M1 6h10M6 1c-3 3-3 7 0 10M6 1c3 3 3 7 0 10" fill="none" stroke-width="1" style="stroke:var(--ink)"/></svg>
        www.innerway.com
      </li>
    </ul>
  </section>
</main>
</body>
</html>
```